Pelwick Renovations Letterhead

Pelwick does not do actual renovation, but rather handles high end project management of renovation (primarily residential with an eye toward commercial and International) The renovation work could look very different between projects. This company works directly with the clients and manages the work of contractors, architects and interior designers (either subcontracted directly by Pelwick or hired by the client and entrusted to Pelwick to manage). Clients are high end in the economic scale and all materials should speak to that audience. Provoke a sense of change, openness and imagination, trust and integrity. The owner is female, but the audience will be heavily slanted male. It should not be a "feminine" or "masculine" looking . If anything, slant more on the masculine side.

Clean, simple, yet creative and artistically appealing. The logo should be clear and not competing with too many surrounding design elements.

There is a contest also on for business card. Please check that section if you would like to compete for both.

Get your creative juices going!

Target Market(s)

High end cients. Additional audience: professionals (architects, etc...) designers, contractors

Industry/Entity Type

Residential

Requirements
Must have
• Logo must be included in all materials

```html
<!DOCTYPE html>
<html lang="en">
<head>
<meta charset="utf-8">
<title>Pelwick Renovations Letterhead</title>
<link rel="stylesheet" href="https://fonts.googleapis.com/css2?family=Mulish:wght@700&family=Tinos&family=Arimo&display=swap">
<style>
  :root {
    --ink: #1c1c1c;
    --green: #34e48c;
    --paper: #ffffff;
    --faint: #ececec;
    --text: #222222;
  }
  * { margin: 0; padding: 0; box-sizing: border-box; }
  html, body { width: 958px; height: 1200px; overflow: hidden; background: var(--paper); }
  .letterhead { position: relative; width: 958px; height: 1200px; background: var(--paper); }

  .brand { position: absolute; left: 27px; top: 72px; display: flex; align-items: center; gap: 12px; }
  .brand-mark { width: 22px; height: 22px; background: var(--green); }
  .brand-name {
    font-family: "Mulish", sans-serif; font-weight: 700; font-size: 25px;
    letter-spacing: 0.5px; color: var(--ink); text-transform: uppercase;
  }

  .address {
    position: absolute; left: 706px; top: 44px; height: 64px;
    border-left: 1.5px solid var(--ink); padding-left: 11px;
    font-family: "Tinos", serif; font-size: 18px; line-height: 23px; color: var(--text);
  }

  .backdrop-name {
    position: absolute; left: 0; right: 0; top: 560px; text-align: center;
    font-family: "Mulish", sans-serif; font-weight: 700; font-size: 120px;
    color: var(--faint); text-transform: uppercase; letter-spacing: 4px;
  }

  .phone {
    position: absolute; left: 0; right: 0; top: 1131px; text-align: center;
    font-family: "Arimo", sans-serif; font-size: 17px; color: var(--text);
    display: flex; justify-content: center; align-items: center; gap: 5px;
  }
  .phone svg { width: 16px; height: 16px; }

  .footer-band { position: absolute; left: 0; top: 1162px; width: 958px; height: 38px; display: flex; }
  .footer-band .side-dark { width: 500px; background: var(--ink); }
  .footer-band .side-green { flex: 1; background: var(--green); }

  .footer-item {
    position: absolute; top: 1162px; height: 38px; display: flex; align-items: center; gap: 7px;
    font-family: "Tinos", serif; font-size: 18px; color: #ffffff;
  }
  .footer-item svg { width: 15px; height: 15px; }
  .footer-email { left: 125px; }
  .footer-web { left: 545px; }
  .footer-name {
    position: absolute; top: 1162px; left: 430px; width: 100px; height: 38px;
    display: flex; align-items: center; justify-content: center;
    font-family: "Mulish", sans-serif; font-weight: 700; font-size: 13px;
    color: #ffffff; text-transform: uppercase; letter-spacing: 1px;
  }
</style>
</head>
<body>
<main class="letterhead">
  <header>
    <div class="brand">
      <span class="brand-mark"></span>
      <span class="brand-name">Pelwick Renovations</span>
    </div>
    <address class="address" style="font-style: normal;">
      47 Alder Ridge Road<br>
      Suite 208<br>
      Linfield, New York 10590
    </address>
  </header>

  <div class="backdrop-name" aria-hidden="true">Pelwick</div>

  <footer>
    <div class="phone">
      <svg viewBox="0 0 16 16" aria-hidden="true">
        <circle cx="8" cy="8" r="7" fill="none" stroke="var(--green)" stroke-width="1.3"/>
        <path d="M6 4.5 L7.5 6.5 L6.8 7.4 Q7.6 9 9 9.6 L9.8 8.8 L11.6 10.2 L10.8 11.5 Q7.5 11.3 5 7 Q4.8 5.2 6 4.5 Z" fill="var(--green)"/>
      </svg>
      <span>555.014.2739</span>
    </div>
    <div class="footer-band"><div class="side-dark"></div><div class="side-green"></div></div>
    <div class="footer-item footer-email">
      <svg viewBox="0 0 16 16" aria-hidden="true">
        <rect x="1" y="4" width="14" height="10" rx="1" fill="#ffffff"/>
        <path d="M1.5 4.5 L8 9.5 L14.5 4.5" fill="none" stroke="var(--ink)" stroke-width="1.3"/>
      </svg>
      <span>hello@pelwickrenovations.com</span>
    </div>
    <div class="footer-name">Pelwick</div>
    <div class="footer-item footer-web">
      <svg viewBox="0 0 16 16" aria-hidden="true" fill="none" stroke="#ffffff" stroke-width="1.1">
        <circle cx="8" cy="8" r="6.5"/>
        <ellipse cx="8" cy="8" rx="3" ry="6.5"/>
        <path d="M1.5 8 H14.5 M2.5 4.8 H13.5 M2.5 11.2 H13.5"/>
      </svg>
      <span>www.pelwick-renovations.com</span>
    </div>
  </footer>
</main>
</body>
</html>
```